Restaurant service company needs a website!

I am looking for a skilled web designer/developer to create a professional, responsive, and easy-to-navigate website for my company, which specializes in servicing restaurant cooking equipment. The site should communicate trust, reliability, and technical expertise to our target audience, restaurant owners, managers, and commercial kitchen operators. I have included the company logos, if any other format for them is needed please let me know.

Target Market(s)

restaurant owners, managers, and commercial kitchen operators

Industry/Entity Type

Commercial Kitchen Equipment Service

Coding

Coded - Design and coding required

Number of Pages Required

1 page

Font styles to use
Serif
Sans Serif

Requirements
Must have
• Contact and service request forms, Click-to-call functionality for mobile, Clean, modern layout with strong visuals, Easy navigation, mobile-friendly
Nice to have
• Testimonials or Reviews, If possible a click-to-text functionality for mobile.
Should not have
• Any mention of Refrigeration or HVAC, "Free Quotes"

```html
<!DOCTYPE html>
<html lang="en">
<head>
<meta charset="utf-8">
<title>Waypoint Restaurant Service</title>
<link href="https://fonts.googleapis.com/css2?family=Poppins:wght@300;400;500;600;700&display=swap" rel="stylesheet">
<style>
:root{
  --teal:#0b5a78;
  --teal-dark:#074a63;
  --teal-soft:#2f7c98;
  --ink:#1d1d1d;
  --muted:#555;
  --line:#d9dde0;
  --night:#151312;
  --star:#f5a623;
  --white:#fff;
}
*{box-sizing:border-box;margin:0;padding:0}
html,body{width:1200px;height:4587px;overflow:hidden}
body{position:relative;font-family:'Poppins',sans-serif;color:var(--ink);background:var(--white)}
.abs{position:absolute}
a{color:inherit;text-decoration:none}

/* header */
.brand{left:68px;top:40px;display:flex;align-items:center;gap:12px}
.brand-box{width:26px;height:26px;background:var(--teal)}
.brand-name{font-weight:600;font-size:25px;color:var(--teal);letter-spacing:.5px;line-height:1}
.brand-sub{display:block;font-size:10px;letter-spacing:3px;margin-top:4px}
.topphone{left:983px;top:16px;display:flex;align-items:center;gap:12px;font-size:18px;font-weight:500}
.iconbox{width:32px;height:32px;border:1.5px solid var(--teal);border-radius:3px;display:flex;align-items:center;justify-content:center}
.nav{top:72px;font-size:12px;color:#222}
.btn{display:flex;align-items:center;justify-content:center;background:var(--teal);color:#fff;font-weight:500;border-radius:3px}
.nav-cta{left:986px;top:64px;width:147px;height:38px;font-size:12px}

/* hero */
.hero{left:0;top:146px;width:1200px;height:678px;background:linear-gradient(180deg,#8c9aa0 0%,#5d7f8c 45%,#0f5d79 100%)}
.hero-txt{left:0;width:1200px;text-align:center;color:#fff}
.hero-welcome{top:440px;font-size:22px;font-weight:300}
.hero-title{top:482px;font-size:84px;font-weight:700;letter-spacing:1px}
.hero-sub{top:584px;font-size:36px;font-weight:600;letter-spacing:12px}
.hero-tag{top:656px;font-size:19px}
.hero-btn{left:516px;top:712px;width:168px;height:44px;border:1.5px solid #fff;border-radius:4px;color:#fff;font-size:17px;display:flex;align-items:center;justify-content:center}

/* headings */
.h2{font-size:46px;font-weight:700;color:var(--teal);line-height:1}
.center{left:0;width:1200px;text-align:center}
.kicker{font-size:19px;color:var(--teal)}
.rule{height:1.5px;background:var(--teal)}

/* about */
.about-media{left:135px;top:955px;width:360px;height:360px;border-radius:24px;background:linear-gradient(135deg,#c9b79a,#6e7b82 55%,#1e2a30)}
.about-text{left:601px;top:1100px;width:470px;font-size:13.5px;line-height:24px;color:#333}
.about-btn{left:601px;top:1275px;width:166px;height:41px;font-size:15px}

/* services */
.dome{left:397px;top:1765px;width:406px;height:202px;border-radius:203px 203px 0 0;background:linear-gradient(180deg,#1c6f8e,#0a4e68);box-shadow:0 14px 20px rgba(0,0,0,.18)}
.dome-in{left:440px;top:1805px;width:320px;height:162px;border-radius:160px 160px 0 0;background:linear-gradient(180deg,#6f8f9c,#3f6b7c)}
.dome-name{left:397px;top:1918px;width:406px;text-align:center;color:#fff;font-weight:600;font-size:17px}
.svc-ico{width:82px;height:82px;border-radius:50%;background:var(--teal);border:4px solid #fff;box-shadow:0 0 0 2px var(--teal);display:flex;align-items:center;justify-content:center}
.svc-lbl{font-size:17px;line-height:20px;color:#222}

/* why */
.why{left:0;top:2156px;width:1200px;height:354px;background:linear-gradient(90deg,#0e5b78,#2c6f88 50%,#0e5b78)}
.why-ico{width:104px;height:104px;border-radius:50%;background:#fff;border:5px solid #b8cfd8;display:flex;align-items:center;justify-content:center}
.why-lbl{top:2434px;width:320px;text-align:center;color:#fff;font-size:22px;font-weight:500}

/* testimonials */
.quote{width:401px;height:201px;background:var(--teal);border-radius:12px;color:#fff;font-size:14px;line-height:24px;padding:60px 30px 0 30px}
.quote-mark{position:absolute;left:24px;top:8px;font-size:90px;line-height:1;color:#4f8aa2;font-weight:700}
.avatar{width:84px;height:84px;border-radius:50%;background:linear-gradient(180deg,#dfe3e5,#9aa6ab);border:3px solid #fff;box-shadow:0 2px 6px rgba(0,0,0,.2)}
.tname{font-size:21px;font-weight:600}
.stars{color:var(--star);font-size:14px;letter-spacing:1px}
.arrow{width:42px;height:42px;border-radius:50%;display:flex;align-items:center;justify-content:center}

/* contact */
.field{border:1px solid var(--line);font-size:12px;color:#555;padding:12px 18px}
.contact-media{left:615px;top:3327px;width:585px;height:511px;background:linear-gradient(120deg,#2c3438,#b4582c 45%,#3a464c 75%,#6b7478);clip-path:polygon(115px 0,100% 0,100% 100%,115px 100%,0 253px)}

/* cta */
.cta{left:56px;top:3943px;width:1078px;height:249px;background:var(--night);border-radius:14px;overflow:hidden;z-index:2}
.cta-media{position:absolute;left:0;top:0;width:554px;height:249px;background:linear-gradient(100deg,#3a2a22,#a4482a 50%,#2a201c)}
.cta-h{position:absolute;left:587px;top:42px;color:#fff;font-size:30px;line-height:42px}
.cta-btn{position:absolute;left:589px;top:175px;width:188px;height:44px;font-size:16px}

/* footer */
.footer{left:0;top:4120px;width:1200px;height:467px;background:var(--teal)}
.fh{font-size:20px;font-weight:600;color:#fff}
.fl{font-size:13px;color:#fff;display:flex;align-items:center;gap:10px}
.fl-ico{width:16px;height:16px;border:1.3px solid #fff;border-radius:2px}
.social{width:38px;height:38px;border-radius:50%;border:1.5px solid #fff}
.ci{width:28px;height:28px;border:1.3px solid #fff;border-radius:3px;display:flex;align-items:center;justify-content:center}
</style>
</head>
<body>

<!-- header -->
<div class="abs brand"><span class="brand-box"></span><span class="brand-name">WAYPOINT<span class="brand-sub">RESTAURANT SERVICE</span></span></div>
<div class="abs topphone"><span class="iconbox"><svg width="16" height="16" viewBox="0 0 24 24"><path d="M6 3l4 4-2 3c1 2 3 4 6 6l3-2 4 4-3 3C10 20 4 14 3 6z" fill="none" stroke="#0b5a78" stroke-width="2"/></svg></span>555 201 7700</div>
<a class="abs nav" style="left:548px" href="#">HOME</a>
<a class="abs nav" style="left:637px" href="#about">ABOUT US</a>
<a class="abs nav" style="left:753px" href="#services">SERVICES</a>
<a class="abs nav" style="left:865px" href="#testimonials">TESTIMONIALS</a>
<a class="abs btn nav-cta" href="#contact">CONTACT US</a>

<!-- hero -->
<div class="abs hero" role="img" aria-label="Chefs working in a commercial kitchen, tinted teal"></div>
<div class="abs hero-txt hero-welcome">WELCOME TO</div>
<div class="abs hero-txt hero-title">WAYPOINT</div>
<div class="abs hero-txt hero-sub">RESTAURANT SERVICE</div>
<div class="abs hero-txt hero-tag">Keep Your kitchen Running Smoothly</div>
<a class="abs hero-btn" href="#contact">CONTACT US</a>

<!-- about -->
<div class="abs about-media" role="img" aria-label="Kitchen burner graphic filled with a cooking photo"></div>
<h2 class="abs h2" id="about" style="left:601px;top:972px">ABOUT US</h2>
<div class="abs kicker" style="left:601px;top:1030px">WHO WE ARE</div>
<div class="abs rule" style="left:740px;top:1044px;width:94px"></div>
<p class="abs about-text">Lorem ipsum dolor sit amet, consectetur adipiscing elit, sed do eiusm od tempor incididunt ut labore et dolore magna aliqua. Quis ipsum suspendisse ultrices gravida. Risus commodo viverra maecenas acc umsan lacus vel facilisis. Lorem ipsum dolor sit amet, consectetur adipiscing elit, sed do eiusmod tempor incididunt ut labore et dolore magna aliqua.</p>
<a class="abs btn about-btn" href="#">KNOW MORE</a>

<!-- services -->
<h2 class="abs h2 center" id="services" style="top:1495px">OUR SERVICES</h2>
<div class="abs kicker center" style="top:1555px">WHAT WE DO</div>
<div class="abs rule" style="left:435px;top:1568px;width:92px"></div>
<div class="abs rule" style="left:673px;top:1568px;width:92px"></div>
<svg class="abs" style="left:350px;top:1700px" width="500" height="270" viewBox="0 0 500 270">
  <path d="M5 268 A245 245 0 0 1 495 268" fill="none" stroke="#c9d5da" stroke-dasharray="3 4"/>
  <line x1="135" y1="73" x2="157" y2="108" stroke="#0b5a78" stroke-width="1.5"/><circle cx="157" cy="108" r="3" fill="#0b5a78"/>
  <line x1="340" y1="68" x2="320" y2="100" stroke="#0b5a78" stroke-width="1.5"/><circle cx="320" cy="100" r="3" fill="#0b5a78"/>
  <line x1="490" y1="180" x2="447" y2="193" stroke="#0b5a78" stroke-width="1.5"/><circle cx="447" cy="193" r="3" fill="#0b5a78"/>
  <line x1="20" y1="175" x2="53" y2="188" stroke="#0b5a78" stroke-width="1.5"/><circle cx="53" cy="188" r="3" fill="#0b5a78"/>
</svg>
<div class="abs dome"></div>
<div class="abs dome-in" role="img" aria-label="Commercial kitchen range photo"></div>
<div class="abs" style="left:582px;top:1858px;width:36px;height:36px;border:2.5px solid #fff;border-radius:3px"></div>
<div class="abs dome-name">WAYPOINT</div>

<div class="abs svc-ico" style="left:400px;top:1668px"><svg width="40" height="40" viewBox="0 0 24 24" fill="none" stroke="#fff" stroke-width="1.6"><path d="M4 20l9-9M14 4a4 4 0 0 0 5 5l-3 3-4-4zM4 4l6 6M20 20l-6-6"/></svg></div>
<div class="abs svc-lbl" style="left:190px;top:1688px;width:198px;text-align:right">Commercial kitchen<br>Equipment Repair</div>
<div class="abs svc-ico" style="left:675px;top:1647px"><svg width="40" height="40" viewBox="0 0 24 24" fill="none" stroke="#fff" stroke-width="1.6"><circle cx="12" cy="12" r="9"/><text x="12" y="14.5" font-size="7" fill="#fff" stroke="none" text-anchor="middle" font-family="Poppins,sans-serif" font-weight="600">24</text></svg></div>
<div class="abs svc-lbl" style="left:768px;top:1664px">Emergency<br>24/7 Services</div>
<div class="abs svc-ico" style="left:839px;top:1806px"><svg width="40" height="40" viewBox="0 0 24 24" fill="none" stroke="#fff" stroke-width="1.6"><circle cx="12" cy="12" r="3"/><path d="M12 3v3M12 18v3M3 12h3M18 12h3M5.6 5.6l2.1 2.1M16.3 16.3l2.1 2.1M5.6 18.4l2.1-2.1M16.3 7.7l2.1-2.1"/></svg></div>
<div class="abs svc-lbl" style="left:935px;top:1822px">Preventive<br>Maintenance</div>
<div class="abs svc-ico" style="left:282px;top:1819px"><svg width="40" height="40" viewBox="0 0 24 24" fill="none" stroke="#fff" stroke-width="1.6"><circle cx="12" cy="12" r="4"/><circle cx="12" cy="12" r="8" stroke-dasharray="3 2"/></svg></div>
<div class="abs svc-lbl" style="left:60px;top:1838px;width:205px;text-align:right">Restaurant kitchen<br>Equipment Installation<br>and set up</div>

<!-- why -->
<div class="abs why" role="img" aria-label="Blurred kitchen photo with teal overlay"></div>
<h2 class="abs h2 center" style="top:2192px;color:#fff">WHY CHOOSE US</h2>
<div class="abs" style="left:565px;top:2262px;width:70px;height:1.5px;background:#9fc0cd"></div>
<div class="abs why-ico" style="left:230px;top:2302px"><svg width="52" height="52" viewBox="0 0 24 24" fill="none" stroke="#0b5a78" stroke-width="1.3"><circle cx="12" cy="9" r="6"/><path d="M12 6l1 2 2 .3-1.5 1.4.4 2.1L12 10.8l-1.9 1 .4-2.1L9 8.3 11 8z"/><path d="M8 14l-2 7 3-1.5 2 2 1-5M16 14l2 7-3-1.5-2 2-1-5"/></svg></div>
<div class="abs why-ico" style="left:548px;top:2302px"><svg width="52" height="52" viewBox="0 0 24 24" fill="none" stroke="#0b5a78" stroke-width="1.3"><circle cx="13" cy="13" r="7"/><path d="M13 9v4l3 2M11 4h4M13 4v2M2 10h4M1 13h4M2 16h4"/></svg></div>
<div class="abs why-ico" style="left:865px;top:2302px"><svg width="56" height="56" viewBox="0 0 24 24" fill="none" stroke="#0b5a78" stroke-width="1.3"><path d="M20 12a8 8 0 1 1-3-6.2M17 3v3h3"/><text x="12" y="14.5" font-size="6.5" fill="#0b5a78" stroke="none" text-anchor="middle" font-family="Poppins,sans-serif" font-weight="600">24/7</text></svg></div>
<div class="abs why-lbl" style="left:122px">Certified Technicians</div>
<div class="abs why-lbl" style="left:440px">Fast Response Time</div>
<div class="abs why-lbl" style="left:757px">24/7 Support</div>

<!-- testimonials -->
<h2 class="abs h2 center" id="testimonials" style="top:2657px">OUR TESTIMONIALS</h2>
<div class="abs kicker center" style="top:2713px">CUSTOMER REVIEWS</div>
<div class="abs rule" style="left:392px;top:2726px;width:95px"></div>
<div class="abs rule" style="left:715px;top:2726px;width:95px"></div>
<div class="abs arrow" style="left:60px;top:2915px;border:1.5px solid var(--teal)"><svg width="12" height="12" viewBox="0 0 12 12"><path d="M8 2L4 6l4 4" stroke="#0b5a78" stroke-width="2" fill="none"/></svg></div>
<div class="abs arrow" style="left:1103px;top:2915px;background:var(--teal)"><svg width="12" height="12" viewBox="0 0 12 12"><path d="M4 2l4 4-4 4" stroke="#fff" stroke-width="2" fill="none"/></svg></div>

<div class="abs quote" style="left:172px;top:2842px"><span class="quote-mark">&ldquo;</span>Lorem ipsum dolor sit amet, con sectetur adi piscing elit. Maece nas ac tellus ac ipsum porta viverra sit amet sed leo. Vivamus eu maurisc onvallis, hendrerit</div>
<div class="abs avatar" role="img" aria-label="Customer portrait" style="left:196px;top:3058px"></div>
<div class="abs tname" style="left:303px;top:3074px">Daniel Reyes</div>
<div class="abs stars" style="left:306px;top:3106px">★★★★★</div>

<div class="abs quote" style="left:631px;top:2842px"><span class="quote-mark">&ldquo;</span>Lorem ipsum dolor sit amet, con sectetur adi piscing elit. Maece nas ac tellus ac ipsum porta viverra sit amet sed leo. Vivamus eu maurisc onvallis, hendrerit</div>
<div class="abs avatar" role="img" aria-label="Customer portrait" style="left:655px;top:3058px"></div>
<div class="abs tname" style="left:762px;top:3074px">Daniel Reyes</div>
<div class="abs stars" style="left:765px;top:3106px">★★★★★</div>

<!-- contact -->
<h2 class="abs h2" id="contact" style="left:75px;top:3352px">CONTACT US</h2>
<div class="abs rule" style="left:75px;top:3424px;width:90px;height:2px"></div>
<p class="abs" style="left:78px;top:3484px;font-size:13px;color:#333">Please fill out the form below and click submit to contact us. Thank you!</p>
<div class="abs field" style="left:75px;top:3540px;width:235px;height:41px">Your Name</div>
<div class="abs field" style="left:330px;top:3540px;width:232px;height:41px">Phone Number</div>
<div class="abs field" style="left:75px;top:3595px;width:487px;height:42px">Email Address</div>
<div class="abs field" style="left:75px;top:3650px;width:487px;height:80px">Message</div>
<a class="abs btn" style="left:75px;top:3773px;width:189px;height:47px;font-size:16px;font-weight:600" href="#">SUBMIT NOW</a>
<div class="abs contact-media" role="img" aria-label="Stainless steel commercial kitchen line with glowing ovens"></div>

<!-- cta + footer -->
<div class="abs footer"></div>
<div class="abs cta">
  <div class="cta-media" role="img" aria-label="Chef flambéing a pan on a gas range"></div>
  <div class="cta-h">SPECIALIZES IN SERVICING<br>RESTAURANT COOKING<br>EQUIPMENT</div>
  <a class="btn cta-btn" href="#contact">CONTACT US</a>
</div>

<div class="abs fh" style="left:220px;top:4278px">QUICK LINKS</div>
<div class="abs" style="left:220px;top:4318px;width:46px;height:2px;background:#fff"></div>
<div class="abs fl" style="left:227px;top:4345px"><span class="fl-ico"></span>About Us</div>
<div class="abs fl" style="left:227px;top:4377px"><span class="fl-ico"></span>Services</div>
<div class="abs fl" style="left:227px;top:4409px"><span class="fl-ico"></span>Why Choose Us</div>
<div class="abs fl" style="left:227px;top:4441px"><span class="fl-ico"></span>Testimonials</div>
<div class="abs fl" style="left:227px;top:4473px"><span class="fl-ico"></span>Contact Us</div>

<div class="abs" style="left:574px;top:4300px;width:52px;height:52px;border:2.5px solid #fff;border-radius:3px"></div>
<div class="abs" style="left:500px;top:4410px;width:200px;text-align:center;color:#fff;font-size:23px;font-weight:600;line-height:1">WAYPOINT<span style="display:block;font-size:10px;letter-spacing:3px;margin-top:6px">RESTAURANT SERVICE</span></div>
<div class="abs social" style="left:533px;top:4481px"></div>
<div class="abs social" style="left:584px;top:4481px"></div>
<div class="abs social" style="left:632px;top:4481px"></div>

<div class="abs fh" style="left:820px;top:4278px">CONTACT US</div>
<div class="abs" style="left:820px;top:4318px;width:46px;height:2px;background:#fff"></div>
<div class="abs fl" style="left:820px;top:4348px;line-height:16px"><span class="ci"><svg width="13" height="13" viewBox="0 0 24 24"><path d="M6 3l4 4-2 3c1 2 3 4 6 6l3-2 4 4-3 3C10 20 4 14 3 6z" fill="none" stroke="#fff" stroke-width="2"/></svg></span><span>CALL US<br>555 201 7734</span></div>
<div class="abs fl" style="left:820px;top:4398px;line-height:16px"><span class="ci"><svg width="13" height="13" viewBox="0 0 24 24"><rect x="3" y="6" width="18" height="12" fill="none" stroke="#fff" stroke-width="2"/><path d="M3 6l9 7 9-7" fill="none" stroke="#fff" stroke-width="2"/></svg></span><span>EMAIL US<br>info@waypointkitchen.com</span></div>
<div class="abs fl" style="left:820px;top:4448px;line-height:16px"><span class="ci"><svg width="13" height="13" viewBox="0 0 24 24"><path d="M12 22s7-7 7-12a7 7 0 0 0-14 0c0 5 7 12 7 12z" fill="none" stroke="#fff" stroke-width="2"/><circle cx="12" cy="10" r="2.5" fill="#fff"/></svg></span><span>Address line Dummy Here<br>Address line Here</span></div>

<div class="abs" style="left:62px;top:4533px;width:1065px;height:1px;background:#7fa9ba"></div>
<div class="abs center" style="top:4553px;font-size:11px;color:#fff">Copyright ©2025 All rights reserved by the company name</div>

</body>
</html>
```